Bright-loop stitchworks Business Card

embroidery printing

Target Market(s)

Businesses and public

Industry/Entity Type

Business

Contact Information for Business Card

Front of card..... Bright-loop stitchworks .... Dorian Felkway..... 868 512-7743.... Email... bright_loopstitchworks@mailvane.net

Back of card..... Bright-loop stitchworks embroidery & artwork

Colors
000000

```html
<!DOCTYPE html>
<html lang="en">
<head>
<meta charset="utf-8">
<title>Bright-loop stitchworks Business Card</title>
<link rel="stylesheet" href="https://fonts.googleapis.com/css2?family=Open+Sans:wght@400;700&display=swap">
<style>
  :root {
    --brown: #7e4520;
    --white: #ffffff;
    --ink: #222222;
    --backdrop: #ece9e6;
  }
  * { box-sizing: border-box; margin: 0; padding: 0; }
  html, body {
    width: 1200px; height: 900px; overflow: hidden;
    background: var(--backdrop);
    font-family: "Open Sans", Arial, sans-serif;
  }
  .canvas { position: relative; width: 1200px; height: 900px; }
  .card {
    position: absolute; overflow: hidden; border-radius: 16px;
    box-shadow: 0 6px 18px rgba(0,0,0,0.18);
  }
  .card-front { left: 78px; top: 34px; width: 588px; height: 364px; background: var(--white); }
  .card-back  { left: 389px; top: 506px; width: 566px; height: 350px; background: var(--brown); }

  .band { position: absolute; left: 0; width: 100%; }
  .card-front .band { top: 29px; height: 99px; background: var(--brown); }
  .card-back .band  { top: 81px; height: 96px; background: var(--white); }

  .pill {
    position: absolute; display: flex; flex-direction: column;
    align-items: center; justify-content: center;
    border-radius: 60px; text-align: center;
  }
  .card-front .pill { left: 136px; top: 22px; width: 332px; height: 106px; background: var(--white); }
  .card-back .pill  { left: 119px; top: 76px; width: 342px; height: 106px; background: var(--brown); }

  .brand-name {
    font-weight: 700; font-size: 28px; line-height: 1.1; letter-spacing: 0.5px;
  }
  .card-front .brand-name { color: var(--brown); }
  .card-back .brand-name  { color: var(--white); }

  .holder-name {
    position: absolute; top: 170px; width: 100%; text-align: center;
    color: var(--brown); font-weight: 700; font-size: 20px;
  }
  .divider {
    position: absolute; top: 220px; left: 50%; width: 194px; margin-left: -97px;
    border-top: 2px dashed var(--brown);
  }
  .contact {
    position: absolute; top: 272px; width: 100%; text-align: center;
    font-size: 15px; line-height: 25px; color: var(--ink);
  }
  .contact .label { color: var(--brown); font-weight: 700; }

  .tagline {
    position: absolute; top: 250px; width: 100%; text-align: center;
    color: var(--white); font-weight: 700; font-size: 22px;
  }
</style>
</head>
<body>
<main class="canvas">
  <section class="card card-front">
    <div class="band"></div>
    <div class="pill"><span class="brand-name">Bright-loop<br>stitchworks</span></div>
    <h1 class="holder-name">DORIAN FELKWAY</h1>
    <div class="divider"></div>
    <p class="contact">
      <span class="label">Phone:</span> 868 512-7743<br>
      <span class="label">Email:</span> bright_loopstitchworks@mailvane.net
    </p>
  </section>

  <section class="card card-back">
    <div class="band"></div>
    <div class="pill"><span class="brand-name">Bright-loop<br>stitchworks</span></div>
    <p class="tagline">EMBROIDERY &amp; ARTWORK</p>
  </section>
</main>
</body>
</html>
```